Manual design

Hello,

I am looking for someone creative to help me design my Real Estate related manual. I am looking for something simple yet impressive. It would be designed around my logo and brand colors and I would also like it to have a local feel, perhaps with photos I could provide of my area/hometown. I am really shooting for an impressive company and branded look, while keeping it neat without too much going on.

I have the content that I would like to include, I am just struggling with the design of the manual in general.

I have attached a copy of my logo, my companys logo, and a publisher file of what I had previously done. Please do not think the design I previously used is something to work off of if you deem it better to use another feel. I am looking for originality, unless you can improve upon my old file. Any questions, please feel free to reach out to me.

The content in the provided brochure will remain the same, it is the design aspect I need help with. Thanks

Target Market(s)

My target market is home sellers aged 25-55, people usually selling their 1st or second home

Industry/Entity Type

Real Estate

Requirements
Must have
• -A simple to read design focused around my logo and colors
-A local sense
Should not have
• Drawings, only real photos

```html
<!DOCTYPE html>
<html lang="en">
<head>
<meta charset="utf-8">
<title>Educated Sellers Guide</title>
<link rel="stylesheet" href="https://fonts.googleapis.com/css2?family=Crimson+Text:ital,wght@0,400;0,600;1,400&family=Arimo:wght@400;700&display=swap">
<style>
:root{
  --navy:#1b3a8c;
  --blue:#2f5bc0;
  --sky:#7ea0e2;
  --pale:#dfe8f8;
  --ink:#1d2433;
  --white:#ffffff;
  --green:#3aa14a;
}
*{margin:0;padding:0;box-sizing:border-box}
html,body{width:804px;height:1200px;overflow:hidden;background:var(--white)}
body{font-family:"Arimo",Arial,sans-serif;color:var(--ink)}
.spread{display:grid;grid-template-columns:repeat(3,252px);grid-template-rows:repeat(6,190px);column-gap:14px;row-gap:8px;padding:10px}
.page{position:relative;overflow:hidden;background:linear-gradient(135deg,var(--navy) 0%,var(--blue) 45%,var(--sky) 100%);box-shadow:0 1px 2px rgba(0,0,0,.35)}
.paper{position:absolute;left:0;top:40px;right:12px;bottom:22px;background:linear-gradient(180deg,var(--white) 70%,var(--pale));border-top-left-radius:120px 34px;border-top-right-radius:6px}
.quote{position:absolute;left:8px;top:5px;width:120px;font:italic 5.5px/1.25 "Crimson Text",Georgia,serif;color:var(--white)}
.quote b{display:block;text-align:right;font-weight:400}
.title{position:absolute;right:18px;top:44px;font:600 15px/1 "Crimson Text",Georgia,serif;color:var(--navy);text-align:right}
.body{position:absolute;left:18px;right:20px;top:66px;font-size:5px;line-height:1.45;color:var(--ink)}
.body p{margin-bottom:3px}
.body ul{list-style:none}
.body li::before{content:"• ";color:var(--blue)}
.brand{position:absolute;left:6px;bottom:5px;display:flex;align-items:center;gap:3px;font:700 5px/1 "Arimo",Arial,sans-serif;color:var(--white)}
.brand i{display:block;width:10px;height:10px;background:var(--white)}
.photo{background:linear-gradient(135deg,#6f8a5a,#3b5d86);position:absolute}
.cover .paper{top:0;right:12px;bottom:22px;border-radius:0}
.cover h1{position:absolute;left:0;right:12px;top:36px;text-align:center;font:600 27px/1.05 "Crimson Text",Georgia,serif;color:var(--navy)}
.toc{position:absolute;left:30px;right:26px;top:66px;font-size:5.5px;line-height:1.55}
.toc div{display:flex;justify-content:space-between;border-bottom:1px dotted #9fb0d8}
table{border-collapse:collapse;width:100%;font-size:5px}
td{border:1px solid #9fb0d8;padding:1px 3px}
</style>
</head>
<body>
<main class="spread">

<section class="page cover">
  <div class="paper"></div>
  <h1>Educated<br>Sellers Guide</h1>
  <div class="brand"><i></i>Harbor Point Realty</div>
</section>

<section class="page">
  <div class="paper"></div>
  <p class="quote">“The secret of getting ahead is getting started, so start today.”<b>– Mark Lane</b></p>
  <h2 class="title">Table of Contents</h2>
  <div class="toc">
    <div><span>Meet Daniel Reyes</span><span>3</span></div>
    <div><span>About Harbor Point Realty</span><span>4</span></div>
    <div><span>How To Qualify A Professional</span><span>5</span></div>
    <div><span>How I Can Help You</span><span>6</span></div>
    <div><span>Marketing Systems</span><span>8</span></div>
    <div><span>Intelligent Home Pricing</span><span>10</span></div>
    <div><span>Preparing Your Home</span><span>12</span></div>
    <div><span>Costs To Prepare</span><span>15</span></div>
    <div><span>Closing Cost Worksheet</span><span>16</span></div>
    <div><span>What I Need From You</span><span>17</span></div>
  </div>
  <div class="brand"><i></i>Harbor Point Realty</div>
</section>

<section class="page">
  <div class="paper"></div>
  <p class="quote">“Work hard and be kind to the people you serve.”<b>– Jo Reed</b></p>
  <div class="photo" style="left:76px;top:42px;width:22px;height:22px" role="img" aria-label="Portrait of the agent"></div>
  <h2 class="title">Meet Daniel Reyes</h2>
  <div class="photo" style="left:14px;top:70px;width:30px;height:22px" role="img" aria-label="Local hometown scene"></div>
  <div class="photo" style="left:14px;top:96px;width:30px;height:22px" role="img" aria-label="Local park photo"></div>
  <div class="photo" style="left:14px;top:122px;width:30px;height:22px" role="img" aria-label="Downtown street photo"></div>
  <div class="body" style="left:50px;top:70px">
    <p>I grew up right here and have helped local families buy and sell homes for over ten years. I know every street, school and park in town.</p>
    <p>My approach is simple: listen first, price smart, market hard and keep you informed at every step of the sale.</p>
    <p>When I am not working you will find me coaching youth soccer or on the lake with my family.</p>
  </div>
  <div class="brand"><i></i>Harbor Point Realty</div>
</section>

<section class="page">
  <div class="paper"></div>
  <p class="quote">“Quality is never an accident; it is the result of effort and care.”<b>– Ann Cole</b></p>
  <h2 class="title">About Harbor Point Realty</h2>
  <div class="photo" style="left:30px;top:64px;width:48px;height:30px" role="img" aria-label="Office building photo"></div>
  <div class="photo" style="left:160px;top:64px;width:48px;height:30px" role="img" aria-label="Team photo"></div>
  <div class="body" style="top:100px">
    <p>Harbor Point Realty is a locally owned brokerage serving sellers across the region with trusted, personal service.</p>
    <p>Our agents share market data, listing tools and buyer leads so your home gets seen by more qualified buyers, faster.</p>
  </div>
  <div class="brand"><i></i>Harbor Point Realty</div>
</section>

<section class="page">
  <div class="paper"></div>
  <p class="quote">“Choose the right partner and the journey becomes easy.”<b>– Sam Hale</b></p>
  <h2 class="title">How To Qualify<br>A Real Estate Professional</h2>
  <div class="body" style="top:78px">
    <ul>
      <li>How many homes did you sell last year?</li>
      <li>What is your average list to sale price ratio?</li>
      <li>How long do your listings stay on the market?</li>
      <li>How will you market my home?</li>
      <li>How often will you update me?</li>
      <li>Can you give me references from past sellers?</li>
      <li>What makes you different from other agents?</li>
    </ul>
  </div>
  <div class="brand"><i></i>Harbor Point Realty</div>
</section>

<section class="page">
  <div class="paper"></div>
  <p class="quote">“Results speak louder than promises.”<b>– Lee Park</b></p>
  <h2 class="title">How I Can Help You</h2>
  <div class="body" style="top:64px">
    <p>My listings sell faster and closer to asking price than the area average.</p>
    <table>
      <tr><td>Days on market</td><td>31</td><td>58</td></tr>
      <tr><td>List to sale ratio</td><td>98%</td><td>94%</td></tr>
      <tr><td>Homes sold</td><td>42</td><td>11</td></tr>
    </table>
  </div>
  <svg style="position:absolute;left:170px;top:120px" width="56" height="42" viewBox="0 0 56 42" role="img" aria-label="Bar chart of results">
    <rect x="4" y="10" width="10" height="30" fill="#2f5bc0"/><rect x="18" y="22" width="10" height="18" fill="#7ea0e2"/>
    <rect x="32" y="6" width="10" height="34" fill="#2f5bc0"/><rect x="46" y="26" width="8" height="14" fill="#7ea0e2"/>
  </svg>
  <div class="brand"><i></i>Harbor Point Realty</div>
</section>

<section class="page">
  <div class="paper"></div>
  <p class="quote">“Small steps every day lead to big results.”<b>– Ray Moss</b></p>
  <h2 class="title">How I Can Help You</h2>
  <div class="body" style="top:64px">
    <p style="color:var(--green);font-weight:700;font-size:7px">★★★★★ ★★★★★</p>
    <p>Seller ratings from recent clients across our area.</p>
    <table>
      <tr><td>Communication</td><td>4.9</td></tr>
      <tr><td>Pricing advice</td><td>4.8</td></tr>
      <tr><td>Marketing</td><td>5.0</td></tr>
    </table>
  </div>
  <div class="brand"><i></i>Harbor Point Realty</div>
</section>

<section class="page">
  <div class="paper"></div>
  <p class="quote">“Good marketing makes the home feel irresistible.”<b>– Tia Brooks</b></p>
  <h2 class="title">Marketing Systems</h2>
  <div class="body" style="top:64px;right:80px">
    <p>Every listing gets a full marketing plan built to reach the most buyers in the shortest time.</p>
    <ul><li>Professional photos</li><li>Online listing network</li><li>Open houses</li><li>Print flyers</li><li>Email campaigns</li></ul>
  </div>
  <svg style="position:absolute;left:180px;top:92px" width="42" height="42" viewBox="0 0 42 42" role="img" aria-label="Pie chart of buyer sources">
    <circle cx="21" cy="21" r="20" fill="#2f5bc0"/>
    <path d="M21 21 L21 1 A20 20 0 0 1 40 26 Z" fill="#3aa14a"/>
    <path d="M21 21 L40 26 A20 20 0 0 1 24 41 Z" fill="#7ea0e2"/>
  </svg>
  <div class="brand"><i></i>Harbor Point Realty</div>
</section>

<section class="page">
  <div class="paper"></div>
  <p class="quote">“Buyers decide in seconds, so first looks matter.”<b>– Kim Ford</b></p>
  <h2 class="title">Marketing Systems Cont.</h2>
  <div class="body" style="top:64px">
    <p>Online exposure: your home appears on every major search site within hours of listing.</p>
    <p>Signs and riders: clear signage with my direct line so buyers can call any time.</p>
    <p>Agent network: I share new listings with local agents who have active buyers.</p>
    <p>Feedback: after each showing I gather buyer comments and share them with you weekly.</p>
  </div>
  <div class="brand"><i></i>Harbor Point Realty</div>
</section>

<section class="page">
  <div class="paper"></div>
  <p class="quote">“Price it right and the market responds.”<b>– Dan Ward</b></p>
  <h2 class="title">Intelligent Home Pricing</h2>
  <svg style="position:absolute;left:20px;top:72px" width="44" height="44" viewBox="0 0 44 44" role="img" aria-label="Pricing target diagram">
    <circle cx="22" cy="22" r="20" fill="none" stroke="#2f5bc0" stroke-width="2"/>
    <circle cx="22" cy="22" r="12" fill="none" stroke="#7ea0e2" stroke-width="2"/>
    <circle cx="22" cy="22" r="4" fill="#1b3a8c"/>
  </svg>
  <div class="body" style="left:72px;top:66px">
    <p>Pricing is the most important choice you will make. A home priced right draws more showings and better offers.</p>
    <p>I compare recent sales, active listings and expired homes nearby to find the price buyers will pay.</p>
    <p>Overpriced homes sit, and stale listings often sell for less in the end.</p>
  </div>
  <div class="brand"><i></i>Harbor Point Realty</div>
</section>

<section class="page">
  <div class="paper"></div>
  <p class="quote">“Know the facts before you sign.”<b>– Eve Long</b></p>
  <h2 class="title">Exclusive Entitlements</h2>
  <div class="body" style="top:64px">
    <p>1. Written pricing analysis before listing.</p>
    <p>2. Weekly updates on showings and feedback.</p>
    <p>3. Full review of every offer received.</p>
    <p>4. Help with inspection and appraisal steps.</p>
    <p>5. Coordination with title and lender to closing.</p>
    <p>6. A cancel any time listing guarantee.</p>
  </div>
  <div class="brand"><i></i>Harbor Point Realty</div>
</section>

<section class="page">
  <div class="paper"></div>
  <p class="quote">“You never get a second chance at a first impression.”<b>– Ian Price</b></p>
  <h2 class="title">Preparing Your Home for Sale</h2>
  <div class="body" style="top:64px;display:flex;gap:12px">
    <ul><li>Clear counters</li><li>Fresh paint</li><li>Fix leaks</li><li>Clean windows</li><li>Trim hedges</li><li>Mow the lawn</li></ul>
    <ul><li>Remove clutter</li><li>Pack photos</li><li>Bright bulbs</li><li>Neat closets</li><li>Clean carpets</li><li>Tidy garage</li></ul>
  </div>
  <div class="brand"><i></i>Harbor Point Realty</div>
</section>

<section class="page">
  <div class="paper"></div>
  <p class="quote">“Preparation is the key to success.”<b>– Joy Banks</b></p>
  <h2 class="title">Preparing Your Home Cont.</h2>
  <div class="body" style="top:64px">
    <p>Curb appeal: buyers judge from the street. Add flowers, paint the front door and sweep the walk.</p>
    <p>Inside: open blinds, air out rooms and set a simple table to help buyers picture living there.</p>
    <p>Showings: leave during visits so buyers feel free to look and talk openly.</p>
  </div>
  <div class="brand"><i></i>Harbor Point Realty</div>
</section>

<section class="page">
  <div class="paper"></div>
  <p class="quote">“Promises kept build trust that lasts.”<b>– Max Dale</b></p>
  <h2 class="title">My Listing Guarantee</h2>
  <div class="body" style="top:64px">
    <p>If I do not deliver the service I promise, you may cancel your listing at any time with no fee.</p>
    <p>I will return calls within one business day, share every offer and keep you updated weekly.</p>
  </div>
  <svg style="position:absolute;left:96px;top:126px" width="60" height="22" viewBox="0 0 60 22" role="img" aria-label="Guarantee seal">
    <rect x="1" y="1" width="58" height="20" rx="4" fill="none" stroke="#2f5bc0" stroke-width="2"/>
  </svg>
  <div class="brand"><i></i>Harbor Point Realty</div>
</section>

<section class="page">
  <div class="paper"></div>
  <p class="quote">“Happy clients are the best advertising.”<b>– Liz Grant</b></p>
  <h2 class="title">A Few Words From Clients</h2>
  <div class="body" style="top:64px">
    <p>“Daniel sold our home in two weeks and above asking. He kept us calm the whole way.” – The Mills</p>
    <p>“Clear advice, great photos and steady updates. We would use him again.” – Sara P.</p>
    <p>“He knew our town and the right price from day one.” – Tom &amp; Ava</p>
  </div>
  <div class="brand"><i></i>Harbor Point Realty</div>
</section>

<section class="page">
  <div class="paper"></div>
  <p class="quote">“Plan ahead and avoid surprises.”<b>– Ned Cruz</b></p>
  <h2 class="title">Items to Prepare in Advance</h2>
  <div class="body" style="top:64px">
    <ul><li>Mortgage statement</li><li>Property tax bill</li><li>Utility costs</li><li>Survey and plat</li><li>Warranty papers</li><li>Repair receipts</li><li>HOA documents</li><li>Spare keys and codes</li></ul>
  </div>
  <div class="brand"><i></i>Harbor Point Realty</div>
</section>

<section class="page">
  <div class="paper"></div>
  <p class="quote">“Know your numbers before you list.”<b>– Ada Stone</b></p>
  <h2 class="title">Closing Cost Worksheet</h2>
  <div class="body" style="top:64px">
    <table>
      <tr><td>Sale price</td><td>$</td></tr>
      <tr><td>Mortgage payoff</td><td>$</td></tr>
      <tr><td>Commission</td><td>$</td></tr>
      <tr><td>Title fees</td><td>$</td></tr>
      <tr><td>Repairs</td><td>$</td></tr>
      <tr><td>Net to seller</td><td>$</td></tr>
    </table>
  </div>
  <div class="brand"><i></i>Harbor Point Realty</div>
</section>

<section class="page">
  <div class="paper"></div>
  <p class="quote">“Together we get it done.”<b>– Bo Hart</b></p>
  <h2 class="title">What I Need From You</h2>
  <div class="body" style="top:64px">
    <ul><li>Keep the home show ready</li><li>Allow flexible showing times</li><li>Tell me about any changes</li><li>Review offers promptly</li><li>Share all known repairs</li><li>Trust the plan and stay in touch</li></ul>
  </div>
  <div class="brand"><i></i>Harbor Point Realty</div>
</section>

</main>
</body>
</html>
```